Beauty & Wellness business needs a flyer to describe a multitude of therapy

I would like a flyer to represent my company. i would like it to have the form of a pamphlet 6 pages. The flyer should be in french if possible, but english also is okay. I'll upload a word file that illustrate what i would like, but it can be of course other images, this is just an example. And the text includes all the services we provide, some small description might be added if you think it's worth it from design point of view.
Target Market(s)
The market is seasonal. it's mostly winter for skiers, so wealthy and sporty people, and attentive to nature. But i also want to promote the brand for locals all year long, with reasonable pricing.
Industry/Entity Type
Wellness & aesthetics
Look and feel

```html
<!DOCTYPE html>
<html lang="fr">
<head>
<meta charset="utf-8">
<title>Liora Studio – Dépliant trois volets</title>
<link rel="stylesheet" href="https://fonts.googleapis.com/css2?family=Marcellus&family=Cinzel:wght@700&family=Crimson+Text:ital,wght@0,400;1,400&family=Playfair+Display:ital,wght@1,600&family=Roboto:wght@400&display=swap">
<style>
:root{
  --stage:#3a3a3c;
  --plum:#6e1d5c;
  --plum-bar:#8a3279;
  --plum-text:#7a2364;
  --mist:#dcd8df;
  --gold:#fcc016;
  --gold-line:#f2c14e;
  --phone:#f7c22b;
  --blush:#f7d5e6;
  --magenta:#e4449b;
  --frame:#e9a3c8;
  --accent-pink:#e9609f;
  --grey-text:#666;
}
*{margin:0;padding:0;box-sizing:border-box}
html,body{width:853px;height:1200px;overflow:hidden;background:var(--stage)}
body{position:relative;font-family:"Crimson Text",Georgia,serif}
h2,h3{font-weight:400}
.label{position:absolute;color:#fff;font-family:"Crimson Text",Georgia,serif;font-size:16px;transform:translateX(-50%);white-space:nowrap}
.sheet{position:absolute;left:136px;width:575px;height:447px;box-shadow:4px 5px 10px rgba(0,0,0,.55)}
.sheet-outside{top:112px}
.sheet-inside{top:603px}
.panel{position:absolute;top:0;height:447px;overflow:hidden}
.abs{position:absolute}
.photo{position:absolute}
.frame{position:absolute;border:1px solid var(--frame)}
.heading{position:absolute;left:0;right:0;text-align:center;font-family:"Marcellus",Georgia,serif;font-weight:400;color:var(--plum-text);line-height:1.05}
.list{position:absolute;text-align:center;font-size:9px;color:var(--plum-text)}
.list li{list-style:none;height:15.5px;line-height:15px;border-bottom:1px solid var(--gold-line)}
.list li:last-child{border-bottom:none}

/* Outside */
.panel-epilation{left:0;width:193px;background:var(--mist)}
.panel-contact{left:193px;width:188px;background:var(--plum)}
.panel-cover{left:381px;width:194px;background:var(--mist)}

.service-bar{position:absolute;left:17px;width:152px;height:21px;background:var(--plum-bar);border-radius:3px;color:#fff;text-align:center;font-family:"Playfair Display",Georgia,serif;font-style:italic;font-weight:600;font-size:13px;line-height:21px}
.feature-card{position:absolute;left:21px;top:112px;width:145px;height:131px;border-radius:4px;background:linear-gradient(180deg,#a6a4a4 0%,#a6a4a4 40%,#9a6656 100%);color:#fff;text-align:center;padding:8px 8px 0}
.feature-card h3{font-family:"Marcellus",Georgia,serif;font-size:10px;line-height:1.1;font-variant:small-caps;letter-spacing:.3px}
.feature-card p{font-size:7px;line-height:1.4;text-align:justify;margin-top:5px}
.contact-title{position:absolute;left:0;right:0;top:316px;text-align:center;color:#fff;font-family:"Playfair Display",Georgia,serif;font-style:italic;font-weight:600;font-size:15px}
.contact-line{position:absolute;left:20px;right:20px;text-align:center;color:#fff;font-family:"Roboto",Arial,sans-serif;font-size:8px;letter-spacing:1.4px}
.contact-rule{position:absolute;left:20px;right:20px;height:1px;background:rgba(255,255,255,.45)}
.contact-phone{position:absolute;left:0;right:0;top:377px;text-align:center;color:var(--phone);font-size:15px}
.contact-address{position:absolute;left:0;right:0;top:402px;text-align:center;color:#fff;font-family:"Roboto",Arial,sans-serif;font-size:7.5px;letter-spacing:.3px}

.brand-mark{position:absolute;left:71px;top:20px;width:52px;height:52px;border:3px solid var(--plum-text);border-radius:50%}
.brand-name{position:absolute;left:0;right:0;top:97px;text-align:center;font-family:"Cinzel",Georgia,serif;font-weight:700;font-size:17px;letter-spacing:3px;color:var(--plum-text)}
.brand-tagline{position:absolute;left:0;right:0;top:123px;text-align:center;font-size:15px;color:var(--grey-text)}
.brand-url{position:absolute;left:28px;right:28px;top:145px;text-align:center;font-size:7.5px;letter-spacing:1px;color:var(--grey-text);border-top:1px solid #b8b3ba;padding-top:2px}

.needling-card{position:absolute;left:24px;top:338px;width:145px;height:89px;border-radius:4px;background:linear-gradient(180deg,#a5694d 0%,#a5694d 45%,#5a5350 100%);color:#fff;padding:6px 10px 0;text-align:center}
.needling-card h3{font-family:"Marcellus",Georgia,serif;font-size:11px;letter-spacing:.8px}
.needling-card p{font-size:7px;line-height:1.35;text-align:justify;margin-top:3px}

/* Inside */
.panel-face{left:0;width:193px;background:#fff}
.panel-massage{left:193px;width:188px;height:297px;background:var(--gold)}
.panel-feet{left:381px;width:194px;height:297px;background:var(--blush)}
.panel-nails{left:193px;top:297px;width:382px;height:150px;background:var(--magenta)}

.massage-list{position:absolute;left:19px;top:41px;font-size:7.5px;color:var(--plum-text)}
.massage-list li{list-style:none;height:12.1px;line-height:12px;display:flex;align-items:center;gap:3px}
.massage-list li::before{content:"";width:6px;height:6px;border-radius:50%;background:radial-gradient(circle at 35% 35%,#eee,#999)}
.thumb{position:absolute;left:117px;width:61px;height:42px;border:1px solid #fff}

.nails-title{position:absolute;left:0;width:156px;top:31px;text-align:center;font-family:"Marcellus",Georgia,serif;font-weight:400;color:#fff;font-size:13.5px;line-height:1.1}
.nails-list{position:absolute;left:22px;width:110px;top:74px;text-align:center;color:#fff;font-size:9px}
.nails-list li{list-style:none;height:15.5px;line-height:15px;border-bottom:1px solid var(--gold-line)}
.nails-list li:last-child{border-bottom:none}
</style>
</head>
<body>

<div class="label" style="left:225px;top:82px">Outside</div>
<div class="label" style="left:417px;top:83px">BACK</div>
<div class="label" style="left:621px;top:82px">FRONT</div>

<section class="sheet sheet-outside">
  <div class="panel panel-epilation">
    <h2 class="heading" style="top:17px;font-size:11.5px">ÉPILATION MASCULINE<br>ET FÉMININ</h2>
    <div class="frame" style="left:27px;top:51px;width:140px;height:177px"></div>
    <svg class="abs" style="left:27px;top:51px" width="140" height="177" aria-hidden="true">
      <polygon points="0,0 75,0 0,45" fill="var(--accent-pink)"/>
    </svg>
    <div class="photo" role="img" aria-label="Photo : épilation du dos à la cire" style="left:32px;top:53px;width:131px;height:80px;background:#7d5a48"></div>
    <div class="photo" role="img" aria-label="Photo : épilation des jambes à la bande" style="left:32px;top:138px;width:131px;height:80px;background:#e2c9bd"></div>
    <svg class="abs" style="left:27px;top:51px" width="140" height="177" aria-hidden="true">
      <polygon points="140,177 140,135 80,177" fill="var(--accent-pink)"/>
    </svg>

    <div class="frame" style="left:27px;top:234px;width:140px;height:96px"></div>
    <h2 class="heading" style="top:240px;font-size:11.5px">DESIGN DES SOURCILS</h2>
    <div class="photo" role="img" aria-label="Photo : mise en forme des sourcils à la pince" style="left:32px;top:253px;width:130px;height:69px;background:#dfc2b1"></div>

    <div class="needling-card" role="img" aria-label="Photo : soin de microneedling du visage">
      <h3>NEEDLING</h3>
      <p>Natural, non-invasive treatment for face and body. Relieve tension and promote collagen production.</p>
    </div>
  </div>

  <div class="panel panel-contact">
    <div class="service-bar" style="top:23px">Thérapie corporelle</div>
    <div class="service-bar" style="top:49px">Thérapie de la peau</div>
    <div class="service-bar" style="top:75px">Esthétique</div>

    <div class="feature-card" role="img" aria-label="Photo : mains laissant tomber de petits diamants">
      <h3>Doigt de diamant<br>gravitationnel</h3>
      <p>Nous livrons la brillance. Notre service de doigt de diamant gravitationnel offre un éclat durable.</p>
    </div>

    <div class="contact-title">Contact</div>
    <div class="contact-line" style="top:340px">www.liora-studio.com</div>
    <div class="contact-rule" style="top:355px"></div>
    <div class="contact-line" style="top:358px;letter-spacing:1.1px;left:10px;right:10px">contact@liora-studio.com</div>
    <div class="contact-rule" style="top:372px"></div>
    <div class="contact-phone">+41-791234567</div>
    <div class="contact-address">Chemin des Alpes 12, Verbier, Suisse</div>
  </div>

  <div class="panel panel-cover">
    <div class="brand-mark" aria-hidden="true"></div>
    <div class="brand-name">LIORA STUDIO</div>
    <div class="brand-tagline">Beauty &amp; Therapy</div>
    <div class="brand-url">www.liora-studio.com</div>
    <div class="photo" role="img" aria-label="Photo : femme aux cheveux bouclés assise, tenant une fleur" style="left:0;top:171px;width:194px;height:276px;background:linear-gradient(180deg,#d9a383 0%,#d9a383 60%,#76744a 60%,#76744a 100%)"></div>
  </div>
</section>

<section class="sheet sheet-inside">
  <div class="panel panel-face">
    <h2 class="heading" style="top:18px;font-size:12.5px">NOS TRAITEMENTS<br>DU VISAGE</h2>
    <div class="frame" style="left:25px;top:48px;width:141px;height:90px"></div>
    <div class="photo" role="img" aria-label="Photo : application d'un masque blanc sur le visage" style="left:30px;top:52px;width:131px;height:81px;background:#ecdfd8"></div>
    <ul class="list" style="left:42px;width:110px;top:144px">
      <li>Soin du visage classique</li>
      <li>Fils de collagènes</li>
      <li>Thérapie au plâtre</li>
      <li>Plasma Lift</li>
    </ul>
    <div class="frame" style="left:27px;top:207px;width:140px;height:81px"></div>
    <div class="photo" role="img" aria-label="Photo : soin de chromothérapie à lumière rouge" style="left:32px;top:212px;width:130px;height:72px;background:#cf1f10"></div>
    <ul class="list" style="left:42px;width:110px;top:293px;color:var(--grey-text)">
      <li>Chromothérapie</li>
      <li>Aromathérapie</li>
      <li>Needling</li>
    </ul>
    <div class="frame" style="left:27px;top:339px;width:140px;height:89px"></div>
    <div class="photo" role="img" aria-label="Photo : soin des sourcils au dermographe" style="left:32px;top:343px;width:130px;height:81px;background:#d8bcae"></div>
  </div>

  <div class="panel panel-massage">
    <h2 class="heading" style="top:18px;font-size:12.5px">NOS MASSAGES MAISONS</h2>
    <ul class="massage-list">
      <li>Sportif</li>
      <li>Pierre chaude</li>
      <li>AryuvédiquePindas</li>
      <li>Guasha</li>
      <li>Bambou</li>
      <li>Drainage lymphatique</li>
      <li>Pour femmes enceintes</li>
      <li>Réflexologie</li>
      <li>Relaxant</li>
      <li>Shiatsu</li>
      <li>Deep tissue</li>
    </ul>
    <div class="thumb" role="img" aria-label="Photo : massage aux pierres chaudes" style="top:41px;background:#c9bcb8"></div>
    <div class="thumb" role="img" aria-label="Photo : massage du visage" style="top:88px;background:#b3a5a3"></div>
    <div class="thumb" role="img" aria-label="Photo : drainage lymphatique" style="top:132px;background:#a9a9b4"></div>
    <div class="thumb" role="img" aria-label="Photo : pochons aux herbes pour massage" style="top:177px;background:#4a4849"></div>
    <div class="frame" style="left:7px;top:229px;width:171px;height:55px;border-color:#f37c3a"></div>
    <div class="photo" role="img" aria-label="Photo : massage du dos" style="left:11px;top:233px;width:72px;height:47px;background:#b4aaa6"></div>
    <div class="photo" role="img" aria-label="Photo : massage aux pochons chauds" style="left:86px;top:233px;width:88px;height:47px;background:#efd6bd"></div>
  </div>

  <div class="panel panel-feet">
    <h2 class="heading" style="top:18px;font-size:12.5px">SPA DES PIEDS</h2>
    <ul class="list" style="left:40px;width:110px;top:37px;color:var(--grey-text)">
      <li>Argile thérapie</li>
      <li>Paraffine</li>
      <li>Plasma</li>
    </ul>
    <div class="frame" style="left:28px;top:89px;width:140px;height:89px"></div>
    <div class="photo" role="img" aria-label="Photo : fauteuils de spa des pieds" style="left:33px;top:93px;width:130px;height:81px;background:#b4b0a9"></div>
    <h2 class="heading" style="top:182px;font-size:12.5px">MÉSO CELLULITE</h2>
    <div class="frame" style="left:28px;top:203px;width:140px;height:82px"></div>
    <div class="photo" role="img" aria-label="Photo : zone traitée contre la cellulite" style="left:33px;top:207px;width:130px;height:73px;background:linear-gradient(90deg,#fff 0%,#fff 25%,#bd8568 25%,#bd8568 75%,#fff 75%)"></div>
  </div>

  <div class="panel panel-nails">
    <h2 class="nails-title">MANICURE &amp;<br>PÉDICURE</h2>
    <ul class="nails-list">
      <li>Semi permanent</li>
      <li>Fibre de verre</li>
      <li>Gel</li>
    </ul>
    <div class="frame" style="left:178px;top:16px;width:186px;height:119px;border-color:#f59ac7"></div>
    <div class="photo" role="img" aria-label="Photo : mains et pieds soignés avec bougies et fleurs" style="left:185px;top:22px;width:172px;height:106px;background:#eadfd3"></div>
  </div>
</section>

<div class="label" style="left:227px;top:1060px">Front inside</div>
<div class="label" style="left:438px;top:1062px">Back inside</div>
<div class="label" style="left:653px;top:1061px">Outside inside</div>

</body>
</html>
```